K7 Electrical Services Ltd Web design

I require a web site for my new electrical contracting company. We are customer service orientated. Offering high value electrical installations, design and maintenance. Focused on custom residential and commercial upgrading. Lighting design and application are paramount in our company's services. Industry leading product use and integration are always on the forefront with our customer client services. As well as energy efficiency.

Target Market(s)

Homebuilders, General Contractors, Property management companies, clients, individuals,

Industry/Entity Type

Electric Company

Coding

Coded - Design and coding required

Number of Pages Required

3 page

Requirements
Must have
• Classic, modern, edgy but not trendy . Appeals to the masse.
• 3 page
• home page
• about page
• gallery page
• ability to contact from the webiste
Nice to have
• open to all types of designs that are relative to the construction industry.
• Black, Grey, metallic ice blue and deep purple colours from the logo.
Should not have
• anything cheesy with cartoon light bulb images.

```html
<!DOCTYPE html>
<html lang="en">
<head>
<meta charset="utf-8">
<title>K7 Electrical Services Ltd</title>
<link href="https://fonts.googleapis.com/css2?family=Open+Sans:wght@300;400;600;700&family=Roboto:wght@300;400&family=Michroma&display=swap" rel="stylesheet">
<style>
:root{
  --purple:#5c2d91;
  --purple-dark:#4a2277;
  --ink:#2b2b2d;
  --footer:#262628;
  --text:#555;
  --muted:#8a8a8a;
  --line:#d8d8d8;
  --bar:#f3f3f3;
  --field:#9a9a9a;
  --page:#ececee;
  --white:#fff;
}
*{box-sizing:border-box;margin:0;padding:0}
html,body{width:1200px;height:2880px;overflow:hidden}
body{background:var(--page);font-family:"Open Sans",Arial,sans-serif;color:var(--text);position:relative}
.abs{position:absolute}
.site{position:absolute;background:var(--white);overflow:hidden}
.site--desktop{left:25px;top:63px;width:814px;height:1621px;box-shadow:0 2px 10px rgba(0,0,0,.15)}
.site--mobile{left:879px;top:154px;width:277px;height:2519px;box-shadow:0 2px 10px rgba(0,0,0,.15)}

/* shared */
.topbar{position:absolute;left:0;top:0;width:100%;background:var(--bar);font-size:7px;color:#777;text-transform:uppercase;letter-spacing:.2px}
.search{position:absolute;right:0;top:0;background:var(--purple);display:flex;align-items:center;justify-content:center}
.brand{display:flex;align-items:center;gap:6px;color:var(--purple);font-family:"Open Sans",Arial,sans-serif;font-weight:700;text-transform:uppercase;letter-spacing:.5px;line-height:1.1}
.brand__mark{width:12px;height:12px;background:var(--purple);flex:none}
.nav{position:absolute;left:0;width:100%;background:var(--purple)}
.nav__item{color:var(--white);font-size:8px;text-transform:uppercase;font-weight:600;position:absolute}
.hero{position:absolute;left:0;width:100%;background:linear-gradient(160deg,#dfe5e4 0%,#c9d2d3 45%,#8797b4 75%,#b9b3aa 100%)}
.hero__caption{position:absolute;left:0;width:100%;background:rgba(110,110,112,.85);color:var(--white);font-family:"Michroma",Arial,sans-serif;font-weight:400;text-align:center;text-transform:uppercase}
.welcome__title{position:absolute;width:100%;text-align:center;font-family:"Roboto",Arial,sans-serif;font-weight:300;color:#444}
.welcome__sub{position:absolute;text-align:center;color:#333;font-weight:600}
.welcome__text{position:absolute;text-align:center;font-style:italic;color:#777}
.offer{position:absolute;width:100%;text-align:center;color:#333}
.offer-box{position:absolute;background:var(--purple);color:var(--white);text-align:center;border:2px solid #7a54ab}
.divider{position:absolute;height:1px;background:var(--line)}
.gallery{position:absolute;left:0;width:100%;background:linear-gradient(135deg,#3b3c40 0%,#55575c 40%,#3e4045 70%,#2f3033 100%)}
.gallery__title{position:absolute;font-family:"Roboto",Arial,sans-serif;font-weight:300;color:var(--white)}
.card{position:absolute;background:var(--white)}
.card__photo{width:100%;background:linear-gradient(150deg,#9fb5c6 0%,#e6e8ea 45%,#6b7c92 100%)}
.card__label{background:#77777a;color:var(--white);font-family:"Roboto",Arial,sans-serif;font-weight:400;display:flex;align-items:center;padding-left:10px}
.card--white .card__label{background:var(--white);color:#555}
.arrow{position:absolute;border-radius:50%;display:flex;align-items:center;justify-content:center}
.footer{position:absolute;left:0;width:100%;background:var(--footer);border-top:4px solid var(--purple);color:#bbb}
.footer__heading{position:absolute;font-weight:700;color:var(--white);text-transform:uppercase;font-size:8px}
.footer__text{position:absolute;font-size:7px;line-height:1.6;color:#aaa}
.footer__text b{color:#ddd}
.links{position:absolute;list-style:none;font-size:7px;line-height:1.75;color:#aaa}
.links li::before{content:"› ";color:var(--purple)}
.field{position:absolute;background:var(--field);color:#333;font-size:7px;padding:4px 6px}
.send{position:absolute;border:1px solid var(--purple);color:var(--purple);font-size:7px;text-transform:uppercase;display:flex;align-items:center;justify-content:center}
.footer__logo{position:absolute;background:var(--white);display:flex;align-items:center;justify-content:center}
.copyright{position:absolute;font-size:7px;color:#888}
.social{position:absolute;display:flex}
.social span{display:block;border-radius:50%;background:#3d3d40;border:1px solid #555}
</style>
</head>
<body>

<!-- Desktop view -->
<div class="site site--desktop">
  <div class="topbar" style="height:31px;line-height:31px;padding-left:109px">Welcome to the electrical services
    <div class="search" style="width:31px;height:31px;right:109px">
      <svg width="12" height="12" viewBox="0 0 12 12"><circle cx="5" cy="5" r="3.5" fill="none" stroke="#fff" stroke-width="1.5"/><line x1="7.5" y1="7.5" x2="11" y2="11" stroke="#fff" stroke-width="1.5"/></svg>
    </div>
  </div>
  <div class="abs" style="left:0;top:31px;width:814px;height:77px">
    <div class="brand abs" style="left:109px;top:22px;font-size:14px;width:200px"><span class="brand__mark"></span>K7 Electrical Services Ltd</div>
    <div class="abs" style="left:520px;top:29px;display:flex;align-items:center;gap:6px;font-size:14px;color:#888;font-family:Roboto,Arial,sans-serif;font-weight:300">
      <svg width="10" height="16" viewBox="0 0 10 16"><path d="M3 1 L6 1 L6 5 L4 6 Q4 10 6 11 L6 15 L3 15 Q0 8 3 1Z" fill="#999"/></svg>001-7788-4521</div>
    <div class="abs" style="left:665px;top:18px;width:42px;height:42px;border:1px solid #555;border-radius:50%;font-size:8px;color:#333;display:flex;align-items:center;justify-content:center;font-weight:600">EN ⌄</div>
  </div>
  <nav class="nav" style="top:108px;height:42px">
    <span class="nav__item" style="left:118px;top:15px">Home</span>
    <span class="nav__item" style="left:184px;top:15px">About Us</span>
    <span class="nav__item" style="left:266px;top:15px">Gallery</span>
    <span class="nav__item" style="left:342px;top:15px">Contact Us</span>
  </nav>
  <div class="hero" style="top:150px;height:369px" role="img" aria-label="Smiling electrician in blue overalls giving a thumbs up in a bright living room">
    <div class="hero__caption" style="top:307px;height:62px;line-height:62px;font-size:26px;letter-spacing:1px">Lorem ipsum dolor sit amet.</div>
  </div>

  <section class="abs" style="left:0;top:519px;width:814px;height:401px">
    <h2 class="welcome__title" style="top:46px;font-size:22px">Welcome To The Electrical Services</h2>
    <p class="welcome__sub" style="left:0;width:814px;top:78px;font-size:11px;font-weight:400;color:#333">Ut enim ad minim veniam, quis nostrud exercitation ullamco laboris nisi ut aliquip ex</p>
    <div class="divider" style="left:0;top:112px;width:814px"></div>
    <svg class="abs" style="left:400px;top:100px" width="16" height="24" viewBox="0 0 16 24"><line x1="3" y1="22" x2="13" y2="2" stroke="#7a54ab" stroke-width="2"/></svg>
    <p class="welcome__text" style="left:130px;width:554px;top:132px;font-size:8px;line-height:1.7">Lorem ipsum dolor sit amet, consectetur adipiscing elit, sed do eiusmod tempor incididunt ut labore et dolore magna aliqua. Ut enim ad minim veniam, quis nostrud exercitation ullamco laboris nisi ut aliquip ex ea commodo consequat. Duis aute irure dolor in reprehenderit in voluptate velit esse cillum dolore eu fugiat nulla pariatur.</p>
    <div class="brand abs" style="left:340px;top:199px;width:140px;font-size:7px;justify-content:center"><span class="brand__mark" style="width:7px;height:7px"></span>K7 Electrical Services Ltd</div>
    <p class="offer" style="top:239px;font-size:11px">We Offer...</p>
    <div class="offer-box" style="left:109px;top:276px;width:596px;height:77px;padding:18px 30px;font-size:8px;line-height:1.6">Lorem ipsum dolor sit amet, consectetur adipiscing elit, sed do eiusmod tempor incididunt ut labore et dolore magna aliqua. Ut enim ad minim veniam, quis nostrud exercitation ullamco laboris nisi ut aliquip ex ea commodo consequat. Duis aute irure dolor in reprehenderit in voluptate velit esse cillum dolore eu fugiat nulla pariatur.</div>
  </section>

  <section class="gallery" style="top:920px;height:367px" role="img" aria-label="Electricians at work on panels and wiring, darkened background">
    <h2 class="gallery__title" style="left:109px;top:38px;font-size:20px">Electrical Services Gallery</h2>
    <div class="arrow" style="left:74px;top:159px;width:18px;height:18px;background:var(--purple)"><svg width="6" height="8" viewBox="0 0 6 8"><path d="M5 0L1 4L5 8" fill="none" stroke="#fff" stroke-width="1.5"/></svg></div>
    <div class="arrow" style="left:722px;top:159px;width:18px;height:18px;background:var(--white)"><svg width="6" height="8" viewBox="0 0 6 8"><path d="M1 0L5 4L1 8" fill="none" stroke="#333" stroke-width="1.5"/></svg></div>
    <div class="card" style="left:109px;top:83px;width:194px;height:192px"><div class="card__photo" style="height:146px" role="img" aria-label="Electrician in a hard hat working on wiring"></div><div class="card__label" style="height:46px;font-size:13px">Lorem Ipsum Dolor</div></div>
    <div class="card card--white" style="left:310px;top:83px;width:194px;height:192px"><div class="card__photo" style="height:146px" role="img" aria-label="Electrician kneeling at a distribution panel"></div><div class="card__label" style="height:46px;font-size:13px">Ipsum Dolor Sit Amet</div></div>
    <div class="card card--white" style="left:511px;top:83px;width:194px;height:192px"><div class="card__photo" style="height:146px" role="img" aria-label="Hands stripping a cable with pliers"></div><div class="card__label" style="height:46px;font-size:13px">Dolor Sit Amet Consect</div></div>
  </section>

  <footer class="footer" style="top:1287px;height:334px">
    <h3 class="footer__heading" style="left:109px;top:33px">Contact Address</h3>
    <p class="footer__text" style="left:109px;top:52px;width:170px">Lorem ipsum dolor sit amet, consectetur adipiscing elit, sed do eiusmod tempor incididunt ut labore et dolore magna aliqua. Ut enim ad minim veniam.</p>
    <p class="footer__text" style="left:109px;top:120px;width:190px">Lorem Ipsum Dolor Sit Amet Consectetur<br>Dolor Sit Amet Consectetur<br><b>Telp</b> &nbsp;: 014 552 7700 / 014 552 7701<br><b>Fax</b> &nbsp;&nbsp;: 014 552 7710<br><b>Email</b> : hello@k7electrical.example</p>
    <h3 class="footer__heading" style="left:305px;top:33px">Quick Links</h3>
    <ul class="links" style="left:305px;top:50px"><li>Home</li><li>About Us</li><li>Services</li><li>Gallery</li><li>Contact Us</li></ul>
    <h3 class="footer__heading" style="left:453px;top:33px">Contact Us</h3>
    <div class="field" style="left:453px;top:63px;width:121px;height:26px">Name</div>
    <div class="field" style="left:584px;top:63px;width:121px;height:26px">Email</div>
    <div class="field" style="left:453px;top:98px;width:252px;height:65px">How Can We Help?</div>
    <div class="send" style="left:453px;top:178px;width:75px;height:29px">Send</div>
    <p class="copyright" style="left:453px;width:252px;top:233px;text-align:right">© 2018 K7 Electrical Services Ltd. All Rights are Reserved.</p>
    <div class="footer__logo" style="left:109px;top:232px;width:163px;height:61px"><div class="brand" style="font-size:10px;width:140px"><span class="brand__mark" style="width:9px;height:9px"></span>K7 Electrical Services Ltd</div></div>
    <div class="social" style="left:515px;top:258px;gap:10px" aria-label="Social links"><span style="width:40px;height:40px"></span><span style="width:40px;height:40px"></span><span style="width:40px;height:40px"></span><span style="width:40px;height:40px"></span></div>
  </footer>
</div>

<!-- Mobile view -->
<div class="site site--mobile">
  <div class="topbar" style="height:33px;line-height:33px;padding-left:8px;font-size:6px">Welcome to the electrical services
    <div class="search" style="width:30px;height:33px"><svg width="10" height="10" viewBox="0 0 12 12"><circle cx="5" cy="5" r="3.5" fill="none" stroke="#fff" stroke-width="1.5"/><line x1="7.5" y1="7.5" x2="11" y2="11" stroke="#fff" stroke-width="1.5"/></svg></div>
  </div>
  <div class="brand abs" style="left:58px;top:55px;width:170px;font-size:12px;justify-content:center"><span class="brand__mark" style="width:10px;height:10px"></span>K7 Electrical Services Ltd</div>
  <nav class="nav" style="top:106px;height:44px">
    <svg class="abs" style="right:10px;top:15px" width="16" height="14" viewBox="0 0 16 14"><rect y="1" width="16" height="2" fill="#fff"/><rect y="6" width="16" height="2" fill="#fff"/><rect y="11" width="16" height="2" fill="#fff"/></svg>
  </nav>
  <div class="hero" style="top:150px;height:278px" role="img" aria-label="Smiling electrician in blue overalls giving a thumbs up">
    <div class="hero__caption" style="top:244px;height:34px;line-height:34px;font-size:11px">Lorem ipsum dolor sit amet.</div>
  </div>

  <section class="abs" style="left:0;top:428px;width:277px;height:570px">
    <h2 class="welcome__title" style="top:60px;font-size:21px;line-height:1.3;padding:0 10px">Welcome To The Electrical Services</h2>
    <p class="welcome__sub" style="left:10px;width:257px;top:118px;font-size:11px;font-weight:400;line-height:1.25">Ut enim ad minim veniam, quis nostrud exercitation ullamco laboris nisi ut aliquip</p>
    <div class="divider" style="left:0;top:182px;width:277px"></div>
    <svg class="abs" style="left:131px;top:168px" width="16" height="26" viewBox="0 0 16 24"><line x1="3" y1="22" x2="13" y2="2" stroke="#7a54ab" stroke-width="2"/></svg>
    <p class="welcome__text" style="left:15px;width:247px;top:205px;font-size:7px;line-height:1.6">Lorem ipsum dolor sit amet, consectetur adipiscing elit, sed do eiusmod tempor incididunt ut labore et dolore magna aliqua. Ut enim ad minim veniam, quis nostrud exercitation ullamco laboris nisi ut aliquip ex ea commodo consequat. Duis aute irure dolor in reprehenderit in voluptate velit esse cillum dolore eu fugiat nulla pariatur.</p>
    <div class="brand abs" style="left:78px;top:323px;width:120px;font-size:6px;justify-content:center"><span class="brand__mark" style="width:6px;height:6px"></span>K7 Electrical Services Ltd</div>
    <p class="offer" style="top:366px;font-size:10px">We Offer...</p>
    <div class="offer-box" style="left:15px;top:403px;width:248px;height:111px;padding:14px 12px;font-size:7px;line-height:1.55">Lorem ipsum dolor sit amet, consectetur adipiscing elit, sed do eiusmod tempor incididunt ut labore et dolore magna aliqua. Ut enim ad minim veniam, quis nostrud exercitation ullamco laboris nisi ut aliquip ex ea commodo consequat. Duis aute irure dolor in reprehenderit in voluptate velit esse cillum dolore eu fugiat nulla pariatur.</div>
  </section>

  <section class="gallery" style="top:998px;height:774px" role="img" aria-label="Electricians at work, darkened background">
    <h2 class="gallery__title" style="left:12px;top:42px;font-size:17px">Electrical Services Gallery</h2>
    <div class="card" style="left:35px;top:86px;width:196px;height:198px"><div class="card__photo" style="height:150px" role="img" aria-label="Electrician in a hard hat working on wiring"></div><div class="card__label" style="height:48px;font-size:13px">Lorem Ipsum Dolor</div></div>
    <div class="card card--white" style="left:35px;top:311px;width:196px;height:198px"><div class="card__photo" style="height:150px" role="img" aria-label="Electrician kneeling at a distribution panel"></div><div class="card__label" style="height:48px;font-size:13px">Ipsum Dolor Sit Amet</div></div>
    <div class="card card--white" style="left:35px;top:538px;width:196px;height:198px"><div class="card__photo" style="height:150px" role="img" aria-label="Hands stripping a cable with pliers"></div><div class="card__label" style="height:48px;font-size:13px">Dolor Sit Amet Consect</div></div>
  </section>

  <footer class="footer" style="top:1772px;height:747px">
    <h3 class="footer__heading" style="left:12px;top:44px">Contact Address</h3>
    <p class="footer__text" style="left:12px;top:66px;width:170px">Lorem ipsum dolor sit amet, consectetur adipiscing elit, sed do eiusmod tempor incididunt ut labore et dolore magna aliqua. Ut enim ad minim veniam.</p>
    <p class="footer__text" style="left:12px;top:140px;width:250px">Lorem Ipsum Dolor Sit Amet Consectetur<br>Dolor Sit Amet Consectetur<br><b>Telp</b> &nbsp;: 014 552 7700 / 014 552 7701<br><b>Fax</b> &nbsp;&nbsp;: 014 552 7710<br><b>Email</b> : hello@k7electrical.example</p>
    <h3 class="footer__heading" style="left:12px;top:236px">Quick Links</h3>
    <ul class="links" style="left:12px;top:256px"><li>Home</li><li>About Us</li><li>Services</li><li>Gallery</li><li>Contact Us</li></ul>
    <h3 class="footer__heading" style="left:12px;top:355px">Contact Us</h3>
    <div class="field" style="left:12px;top:390px;width:121px;height:25px">Name</div>
    <div class="field" style="left:144px;top:390px;width:121px;height:25px">Email</div>
    <div class="field" style="left:12px;top:426px;width:253px;height:63px">How Can We Help?</div>
    <div class="send" style="left:12px;top:508px;width:75px;height:27px">Send</div>
    <div class="footer__logo" style="left:12px;top:558px;width:165px;height:65px"><div class="brand" style="font-size:10px;width:140px"><span class="brand__mark" style="width:9px;height:9px"></span>K7 Electrical Services Ltd</div></div>
    <p class="copyright" style="left:12px;top:642px;font-size:6px">© 2018 K7 Electrical Services Ltd. All Rights are Reserved.</p>
    <div class="social" style="left:12px;top:680px;gap:8px" aria-label="Social links"><span style="width:42px;height:42px"></span><span style="width:42px;height:42px"></span><span style="width:42px;height:42px"></span><span style="width:42px;height:42px"></span></div>
  </footer>
</div>

</body>
</html>
```